Website to showcase Pram Trail Races that will be held in Woodland Trust Board areas in the UK

Looking for a website, designed in WordPress, to provide information on family orientated running events that I'm organising in the UK (I've registered the website address pramtrailraces.co.uk). Refer to the Project Brief document however as a summary:
These events are unique, as they are for people running with a child in a buggy (or in a wheelchair) and will be on carefully designed, traffic-free courses in Woodland Trust Board areas. The events, by using a specialist timing system, will allow runners to start within a two hour window therefore removing the anxiety / rush to get to the start line for the mass start. All events will be centred around a family day with face painting, adventure playgrounds, café and ample parking. Current thinking is a home page that will contain links to four separate pages, information about me and a blog from my Chatterly and Quibbler feeds, one page for two running events being held at Fern Cottage, Marlow Woods (www.woodlandboard.example/ferncottage) in October and December and another page for an event at Rowan Dell Woods (www.woodlandboard.example/rowandell) in November. The third page will be information on the different running buggies available and how people can come and view them at each event and try them out on the course and if they like it they can purchase that buggy for a 10% discount of the RRP. They will need to email me to reserve a buggy for use at the event. The forth page will be information on myself ('About Me' and the details from my other website can be used at this stage). There will be a link from each event page to allow people to enter that particular race online from an external website (links to follow). My current website is an online shop selling running buggies (www.pramtrail.co.uk).

I'm also looking for the website to be published (access to cPanel will be given to allow this).

Attached is my current logo (this will be replaced by a new one currently being designed but is nearly identical) so will be replaced before the website goes live. Also attached are a couple of photos to give an idea on running with a buggy and the different types of areas being used. One of the pictures is the lineup of running buggies so could be used on the third page as it was taken at one of the event forests. Also attached are two logos for the Woodland Trust Board that should be on the home page.

Alongside the website I'm also looking for two flyers to be designed to showcase each running event (to be used on Social Media and public locations such as cafes, nurseries, running clubs, gyms). One flyer for Fern Cottage Marlow Woods event on the 1st October 2017 and the second flyer for the Rowan Dell Woods event on the 5th November 2017. Both these flyers will be a separate project and therefore attract additional payment for each. Will look to offer this work to the winning designer.

Target Market(s)

Families

Industry/Entity Type

Events

Number of Pages Required

5+ page

Font styles to use
Sans Serif

Colors

Designer to choose colors to be used in the design.

Requirements
Must have
• Clear and precise information that each buggy running event is family orientated, on an off-road course that has been carefully planned to be used by a buggy. Different page to highlight the event (i've taken a video of each course so people can see what the terrain is like), course map, course distance, hill profile, timings for the day, travel directions, course dates in 2017 and 2018.
• I'm also looking for the website to be published (access to cPanel will be given to allow this).
• Countdown timer to the next event.
Nice to have
• Map of the UK with the locations highlighted (with a link to the event page). More locations to follow during the rest of 2017.
Should not have
• A lot of writing in small font

```html
<!DOCTYPE html>
<html lang="en">
<head>
<meta charset="utf-8">
<title>Pram Trail Races</title>
<link href="https://fonts.googleapis.com/css2?family=Raleway:wght@500;600;700;800&family=Mulish:wght@400;600;700&display=swap" rel="stylesheet">
<style>
:root{
  --orange:#f7941d;
  --text:#4a4a4a;
  --navy:#2a4d8f;
  --sky:#3aa3d8;
  --bar:#2f2f2f;
  --footer:#333333;
  --line:#e4e4e4;
  --pin:#8f8f8f;
  --white:#ffffff;
}
*{box-sizing:border-box;margin:0;padding:0}
html,body{width:1200px;height:2894px;overflow:hidden;background:var(--white)}
body{font-family:'Mulish',sans-serif;color:var(--text);position:relative}

/* header */
.site-header{position:absolute;left:0;top:0;width:1200px;height:124px}
.brand{position:absolute;left:87px;top:22px;display:flex;align-items:center;gap:10px}
.brand-dot{width:82px;height:82px;border-radius:50%;background:var(--orange);flex:none}
.brand-name{font-family:'Raleway',sans-serif;font-weight:700;font-size:34px;color:var(--orange);line-height:1;white-space:nowrap}
.social{position:absolute;right:87px;top:48px;display:flex;gap:10px}
.social span{width:31px;height:31px;border-radius:50%;display:block}

/* nav */
.main-nav{position:absolute;left:0;top:124px;width:1200px;height:54px;background:var(--bar);display:flex;align-items:center;padding-left:87px}
.main-nav a{color:#e8e8e8;text-decoration:none;font-size:15px;margin-right:46px;height:54px;line-height:54px;white-space:nowrap}
.main-nav a.active{background:var(--orange);color:#fff;padding:0 22px;margin-right:40px}

/* hero */
.hero{position:absolute;left:0;top:178px;width:1200px;height:397px;background:linear-gradient(180deg,#4f6b3c 0%,#6f8a52 45%,#9b9a6a 100%)}
.hero-title{position:absolute;left:87px;top:82px;font-family:'Raleway',sans-serif;font-weight:800;font-size:36px;color:#fff;letter-spacing:.5px;line-height:44px}
.hero-copy{position:absolute;left:87px;top:128px;width:440px;font-size:18px;line-height:28px;color:#fff}
.btn-orange{display:inline-block;background:var(--orange);color:#fff;font-family:'Raleway',sans-serif;font-weight:700;text-transform:uppercase;text-decoration:none;text-align:center}
.hero .btn-orange{position:absolute;left:87px;top:222px;width:164px;height:50px;line-height:50px;font-size:18px;border-radius:2px}
.hero-dots{position:absolute;left:87px;top:294px;display:flex;gap:6px}
.hero-dots span{width:20px;height:20px;border-radius:50%;border:2px solid #fff}
.hero-dots span.on{background:#fff}

/* countdown */
.count{position:absolute;top:517px;width:134px;height:134px;border-radius:50%;background:var(--orange);border:4px solid #fff;color:#fff;text-align:center}
.count b{display:block;font-family:'Raleway',sans-serif;font-weight:500;font-size:38px;margin-top:28px;line-height:44px}
.count small{display:block;font-size:11px;text-transform:uppercase;margin-top:6px}

/* welcome */
.welcome-title{position:absolute;left:87px;top:706px;font-family:'Raleway',sans-serif;font-weight:700;font-size:34px;color:var(--orange);line-height:44px}
.welcome-copy{position:absolute;left:87px;top:762px;width:690px;font-size:14px;line-height:25px;color:var(--text)}
.btn-ghost{position:absolute;left:87px;top:913px;width:106px;height:42px;border:1px solid #c9c9c9;font-size:13px;line-height:40px;text-align:center;color:#666;text-decoration:none}
.welcome-photo{position:absolute;left:807px;top:718px;width:306px;height:237px;background:linear-gradient(180deg,#8aa3b6 0%,#7b8a80 45%,#5f5446 100%)}

/* events */
.event{position:absolute;top:1042px;height:415px;text-align:center}
.event.fern{left:0;width:598px;background:linear-gradient(180deg,#3d4438 0%,#2e3a26 60%,#262a22 100%)}
.event.rowan{left:604px;width:596px;background:linear-gradient(180deg,#2c2c2a 0%,#5a3a30 30%,#3a3f34 70%,#2e302a 100%)}
.event h3{position:absolute;left:0;right:0;top:112px;font-family:'Raleway',sans-serif;font-weight:700;font-size:28px;line-height:33px;color:var(--orange);text-transform:uppercase}
.event .date{position:absolute;left:0;right:0;top:196px;font-family:'Raleway',sans-serif;font-weight:500;font-size:22px;color:var(--orange);text-transform:uppercase}
.event .btn-orange{position:absolute;left:50%;top:241px;transform:translateX(-50%);width:150px;height:50px;line-height:50px;border-radius:25px;font-size:16px;text-transform:none;font-family:'Mulish',sans-serif}

/* feeds */
.feed{position:absolute;top:1540px;width:500px}
.feed.chatterly{left:87px}
.feed.quibbler{left:620px}
.feed h4{font-family:'Raleway',sans-serif;font-weight:500;font-size:24px;color:var(--navy);margin-bottom:14px}
.feed.quibbler h4{color:var(--sky)}
.post{display:flex;gap:18px;height:130px}
.post .avatar{width:50px;height:40px;background:#efefef;flex:none;position:relative}
.post .avatar::after{content:"";position:absolute;left:12px;top:7px;width:26px;height:26px;border-radius:50%;background:var(--orange)}
.post p{font-size:13px;line-height:19px;color:#444;width:370px}
.actions{display:flex;gap:18px;margin-top:14px;font-size:11px;color:#444;font-weight:600;border-top:1px solid var(--line);border-bottom:4px solid #f2f2f2;width:212px;padding:8px 0 10px}
.meta{font-size:11px;color:#999;margin-top:14px}
.meta a{color:var(--sky);text-decoration:none}
.scroll{position:absolute;top:1575px;width:8px;height:372px;background:#d8d8d8;border-radius:4px}
.scroll::after{content:"";position:absolute;left:-4px;top:130px;width:16px;height:64px;background:#9a9a9a;border-radius:6px}

/* map */
.map{position:absolute;left:0;top:2057px;width:1200px;height:406px;background:linear-gradient(135deg,#e6e6e6 0%,#d9d9d9 50%,#e4e4e4 100%)}
.map svg{position:absolute;left:0;top:0}
.map-zoom{position:absolute;right:10px;bottom:8px;width:22px;height:22px;background:#fff;border:1px solid #ccc;font-size:14px;line-height:20px;text-align:center;color:#666}

/* footer */
.site-footer{position:absolute;left:0;top:2476px;width:1200px;height:418px;background:var(--footer)}
.badge-a{position:absolute;left:87px;top:68px;width:179px;height:104px;background:#8dbf2b}
.badge-b{position:absolute;left:316px;top:100px;width:296px;height:38px;background:#8dbf2b;transform:rotate(-2deg)}
.footer-brand{position:absolute;right:87px;top:64px;display:flex;align-items:center;gap:12px}
.footer-brand .brand-dot{background:#fff;width:88px;height:88px}
.footer-brand .brand-name{color:#fff;font-size:32px}
.signup{position:absolute;right:87px;top:180px;display:flex}
.signup input{width:216px;height:40px;background:#2a2a2a;border:1px solid #555;color:#999;font-family:'Mulish',sans-serif;font-size:13px;padding:0 14px}
.signup button{width:102px;height:40px;background:var(--orange);border:0;color:#fff;font-family:'Raleway',sans-serif;font-weight:700;font-size:16px}
.footer-rule{position:absolute;left:87px;top:247px;width:1026px;height:1px;background:#666}
.footer-nav{position:absolute;left:0;top:287px;width:1200px;display:flex;justify-content:center}
.footer-nav a{color:#ddd;font-size:15px;text-decoration:none;margin:0 23px;white-space:nowrap}
.copyright{position:absolute;left:0;top:338px;width:1200px;text-align:center;font-size:12px;color:#ccc}
</style>
</head>
<body>

<header class="site-header">
  <div class="brand"><span class="brand-dot"></span><span class="brand-name">pramtrail.co.uk</span></div>
  <div class="social" aria-label="Social links">
    <span style="background:#3b5998"></span>
    <span style="background:#3aa3d8"></span>
    <span style="background:#dd4b39"></span>
    <span style="background:#cc2020"></span>
    <span style="background:#b8338a"></span>
  </div>
</header>

<nav class="main-nav">
  <a class="active" href="#">Home</a>
  <a href="#">Fern Cottage Running Event</a>
  <a href="#">Rowan Dell Running Event</a>
  <a href="#">Our Information</a>
  <a href="#">About Us</a>
  <a href="#">Contact Us</a>
</nav>

<section class="hero" role="img" aria-label="Photo of a smiling toddler in a running buggy on a grassy woodland trail">
  <h1 class="hero-title">PRAM TRAIL RACES</h1>
  <p class="hero-copy">Pram Trail Races is a brand new concept developed by Tom Hale, a competitive runner and father of a tireless daughter.</p>
  <a class="btn-orange" href="#">Read more</a>
  <div class="hero-dots"><span class="on"></span><span></span><span></span></div>
</section>

<div class="count" style="left:328px"><b>09</b><small>Day(s)</small></div>
<div class="count" style="left:469px"><b>14</b><small>Hour(s)</small></div>
<div class="count" style="left:612px"><b>64</b><small>Minute(s)</small></div>
<div class="count" style="left:755px"><b>73</b><small>Second(s)</small></div>

<h2 class="welcome-title">Welcome to Pram Trail Races</h2>
<p class="welcome-copy">Pellentesque a imperdiet dolor, et auctor est. Fusce sollicitudin lorem et luctus volutpat. Proin placerat dapibus gravida. In tristique tristique nulla eget hendrerit. Maecenas vel tortor accumsan quam varius imperdiet vel eget elit. Aenean facilisis tincidunt lectus, id dictum nisi luctus eget. Vivamus efficitur ex condimentum, malesuada eros eget, feugiat nibh. Sed tellus ex, imperdiet eget gravida sit amet, volutpat eget turpis. In nec ultricies est. Etiam mattis augue vehicula odio posuere.</p>
<a class="btn-ghost" href="#">Read more</a>
<div class="welcome-photo" role="img" aria-label="Family photo of a runner with his daughter and dog on a beach"></div>

<section class="event fern" role="img" aria-label="Runners pushing buggies on a grassy woodland course">
  <h3>Fern Cottage<br>Running Events</h3>
  <p class="date">October and December 2017</p>
  <a class="btn-orange" href="#">Read More</a>
</section>
<section class="event rowan" role="img" aria-label="Line-up of running buggies in front of a wooden lodge">
  <h3>Rowan Dell<br>Running Event</h3>
  <p class="date">November 2017</p>
  <a class="btn-orange" href="#">Read More</a>
</section>

<section class="feed chatterly">
  <h4>Chatterly</h4>
  <div class="post"><span class="avatar"></span><div><p>Lorem Ipsum is simply dummy text of the printing and typesetting industry. Lorem Ipsum has been the industry's standard dummy text ever since the 1500s</p><div class="actions"><span>Like</span><span>Comment</span><span>Share</span></div></div></div>
  <div class="post"><span class="avatar"></span><div><p>Lorem Ipsum is simply dummy text of the printing and typesetting industry. Lorem Ipsum has been the industry's standard dummy text ever since the 1500s</p><div class="actions"><span>Like</span><span>Comment</span><span>Share</span></div></div></div>
  <div class="post"><span class="avatar"></span><div><p>Lorem Ipsum is simply dummy text of the printing and typesetting industry. Lorem Ipsum has been the industry's standard dummy text ever since the 1500s</p><div class="actions"><span>Like</span><span>Comment</span><span>Share</span></div></div></div>
</section>
<div class="scroll" style="left:552px"></div>

<section class="feed quibbler">
  <h4>Quibbler</h4>
  <div class="post"><span class="avatar"></span><div><p>Lorem Ipsum is simply dummy text of the printing and typesetting industry. Lorem Ipsum has been the industry's standard dummy text ever since the 1500s</p><p class="meta">52 mins ago · <a href="#">Reply</a> · <a href="#">Retweet</a> · <a href="#">Favorite</a></p></div></div>
  <div class="post"><span class="avatar"></span><div><p>Lorem Ipsum is simply dummy text of the printing and typesetting industry. Lorem Ipsum has been the industry's standard dummy text ever since the 1500s</p><p class="meta">52 mins ago · <a href="#">Reply</a> · <a href="#">Retweet</a> · <a href="#">Favorite</a></p></div></div>
  <div class="post"><span class="avatar"></span><div><p>Lorem Ipsum is simply dummy text of the printing and typesetting industry. Lorem Ipsum has been the industry's standard dummy text ever since the 1500s</p><p class="meta">52 mins ago · <a href="#">Reply</a> · <a href="#">Retweet</a> · <a href="#">Favorite</a></p></div></div>
</section>
<div class="scroll" style="left:1082px"></div>

<div class="map" role="img" aria-label="Location map of the UK with pins marking each event venue">
  <svg width="1200" height="406" viewBox="0 0 1200 406" aria-hidden="true">
    <defs>
      <g id="pin">
        <path d="M0 0c-10 0-18 8-18 18 0 13 18 32 18 32s18-19 18-32C18 8 10 0 0 0z" fill="var(--pin)"/>
        <circle cx="0" cy="18" r="6" fill="#e6e6e6"/>
      </g>
    </defs>
    <use href="#pin" x="234" y="118"/>
    <use href="#pin" x="467" y="83"/>
    <use href="#pin" x="571" y="209"/>
    <use href="#pin" x="828" y="64"/>
    <use href="#pin" x="849" y="124"/>
    <use href="#pin" x="944" y="195"/>
    <use href="#pin" x="832" y="292"/>
  </svg>
  <div class="map-zoom">+</div>
</div>

<footer class="site-footer">
  <div class="badge-a" role="img" aria-label="Partner badge"></div>
  <div class="badge-b" role="img" aria-label="Partner badge"></div>
  <div class="footer-brand"><span class="brand-dot"></span><span class="brand-name">pramtrail.co.uk</span></div>
  <form class="signup"><input type="text" placeholder="Enter your email"><button type="button">SIGN UP</button></form>
  <div class="footer-rule"></div>
  <nav class="footer-nav">
    <a href="#">Home</a><a href="#">Fern Cottage Running Event</a><a href="#">Rowan Dell Running Event</a><a href="#">Our Information</a><a href="#">About Us</a><a href="#">Contact Us</a>
  </nav>
  <p class="copyright">Copyright © 2017. Pram Trail Races. All rights reserved.</p>
</footer>

</body>
</html>
```